Business Card Design

We need a business card design for a Dry cleaners in Brisbane, Australia. We are trying to promote a fresh/clean image consistent with our website. www.finchlanelaundry.com.au

Looking for a professional neat card that's easy to read.

Target Market(s)

Customers looking for a professional, fresh and clean drycleaners.

Industry/Entity Type

Business

Contact Information for Business Card

See our existing business card. The Fax number (07) 3648 2051 to be removed.

Requirements
Must have
• All the details on current business card less the fax number.
Nice to have
• I like white text on coloured background. Blue works well as we are located near the water...

```html
<!DOCTYPE html>
<html lang="en">
<head>
<meta charset="utf-8">
<title>Finch Lane Laundry – Business Card</title>
<link rel="stylesheet" href="https://fonts.googleapis.com/css2?family=Arimo:wght@400;700&display=swap">
<style>
  :root {
    --bay-blue: #156bb6;
    --card-white: #ffffff;
    --backdrop: #e9e9e9;
    --ink-light: #ffffff;
  }
  html, body {
    margin: 0;
    padding: 0;
    width: 1200px;
    height: 800px;
    overflow: hidden;
    background: var(--backdrop);
    font-family: "Arimo", Arial, sans-serif;
  }
  .business-card {
    position: absolute;
    left: 82px;
    top: 80px;
    width: 1036px;
    height: 640px;
    background: var(--card-white);
    overflow: hidden;
  }
  .card-waves {
    position: absolute;
    inset: 0;
    width: 100%;
    height: 100%;
  }
  .card-waves .wave { fill: var(--bay-blue); }
  .brand-name {
    position: absolute;
    left: 68px;
    top: 150px;
    margin: 0;
    font-size: 54px;
    line-height: 62px;
    font-weight: 700;
    color: var(--bay-blue);
    letter-spacing: 0.5px;
  }
  .holder {
    position: absolute;
    left: 68px;
    top: 496px;
    color: var(--ink-light);
  }
  .holder-name {
    margin: 0;
    font-size: 48px;
    font-weight: 400;
    letter-spacing: 2px;
    line-height: 56px;
  }
  .holder-email {
    margin: 12px 0 0;
    font-size: 26px;
    line-height: 30px;
  }
  .contact-list {
    position: absolute;
    left: 732px;
    top: 412px;
    margin: 0;
    padding: 0;
    list-style: none;
    color: var(--ink-light);
    font-size: 26px;
    line-height: 34.5px;
    letter-spacing: 1px;
  }
</style>
</head>
<body>
  <div class="business-card">
    <svg class="card-waves" viewBox="0 0 518 320" preserveAspectRatio="none" aria-hidden="true">
      <path class="wave wave-stripe" d="M0,217 C150,207 390,160 518,63 L518,77 C390,172 150,222 0,233 Z"/>
      <path class="wave wave-base" d="M0,243 C150,233 385,182 518,92 L518,320 L0,320 Z"/>
    </svg>

    <h1 class="brand-name">Finch Lane Laundry</h1>

    <div class="holder">
      <p class="holder-name">Maren Tolley</p>
      <p class="holder-email">E:maren@finchlanelaundry.com.au</p>
    </div>

    <ul class="contact-list">
      <li>M: 0412 658 903</li>
      <li>27 Kestrel Rd</li>
      <li>Lota Qld 4179</li>
      <li>P: (07) 3527 4806</li>
    </ul>
  </div>
</body>
</html>
```